Lucien Dorval

Changes to attached business card: 1. Eliminate borders (black) top and bottom of the existing card. 2- eliminate: Become the reference! 3- adding: www.boostezvoschiffres.ca info@boostezvoschiffres.ca luciendorvalconseil.com (819) 555-2731 4- black on white

Contact Information for Business Card

voir pièce ci-jointe pour exemple

Requirements
Must have
• black on white
Nice to have
• Very modern ! with punch!

```html
<!DOCTYPE html>
<html lang="fr">
<head>
<meta charset="utf-8">
<title>Lucien Dorval – Carte professionnelle</title>
<link rel="stylesheet" href="https://fonts.googleapis.com/css2?family=Cinzel:wght@600&family=Lato:wght@400&family=Libre+Baskerville:wght@400;700&display=swap">
<style>
  :root {
    --backdrop: #3a3b37;
    --card: #ffffff;
    --ink: #141414;
    --ink-soft: #333333;
    --rule: #c9c9c9;
  }
  * { margin: 0; padding: 0; box-sizing: border-box; }
  html, body {
    width: 1200px;
    height: 1140px;
    overflow: hidden;
    background: var(--backdrop);
  }
  .canvas {
    position: relative;
    width: 1200px;
    height: 1140px;
  }
  .card {
    position: absolute;
    left: 245px;
    width: 707px;
    height: 401px;
    background: var(--card);
    border-radius: 20px;
    color: var(--ink);
    text-align: center;
  }
  .card--front { top: 111px; }
  .card--back { top: 612px; }
  .line {
    position: absolute;
    left: 0;
    right: 0;
    transform: translateY(-50%);
    white-space: nowrap;
  }
  .slogan {
    font-family: "Libre Baskerville", Georgia, serif;
    font-weight: 700;
    font-size: 15px;
    letter-spacing: 0.2px;
  }
  .card--back .slogan { color: var(--ink-soft); font-size: 14px; }
  .sheen {
    position: absolute;
    left: 50%;
    width: 285px;
    height: 3px;
    transform: translate(-50%, -50%);
    background: linear-gradient(90deg, rgba(201,201,201,0) 0%, var(--rule) 50%, rgba(201,201,201,0) 100%);
  }
  .brand-mark {
    position: absolute;
    left: 50%;
    top: 150px;
    width: 56px;
    height: 56px;
    border-radius: 50%;
    background: var(--ink);
    transform: translate(-50%, -50%);
  }
  .brand-name {
    font-family: "Cinzel", "Times New Roman", serif;
    font-weight: 600;
    font-size: 39px;
    color: var(--ink);
  }
  .role {
    font-family: "Lato", Arial, sans-serif;
    font-size: 17px;
    display: flex;
    justify-content: center;
    align-items: center;
    gap: 6px;
  }
  .role::before, .role::after {
    content: "";
    width: 60px;
    height: 1.5px;
    background: var(--ink);
  }
  .site-caps {
    font-family: "Libre Baskerville", Georgia, serif;
    font-weight: 700;
    font-size: 16px;
  }
  .card--back .site-caps { font-size: 15px; color: var(--ink-soft); }
  .icon {
    position: absolute;
    left: 50%;
    width: 28px;
    height: 28px;
    transform: translate(-50%, -50%);
  }
  .contact {
    font-family: "Libre Baskerville", Georgia, serif;
    font-weight: 700;
    font-size: 27px;
    letter-spacing: 0.3px;
    color: var(--ink-soft);
    font-variant-numeric: lining-nums;
  }
</style>
</head>
<body>
<main class="canvas">

  <section class="card card--front" aria-label="Recto">
    <p class="line slogan" style="top:23px">AUGMENTEZ LES VENTES!</p>
    <span class="sheen" style="top:52px"></span>
    <span class="brand-mark" aria-hidden="true"></span>
    <h1 class="line brand-name" style="top:274px">Lucien Dorval</h1>
    <p class="line role" style="top:306px">Consultant - Coach</p>
    <span class="sheen" style="top:345px"></span>
    <p class="line site-caps" style="top:376px">WWW.BOOSTEZVOSCHIFFRES.CA</p>
  </section>

  <section class="card card--back" aria-label="Verso">
    <p class="line slogan" style="top:25px">AUGMENTEZ LES VENTES!</p>

    <svg class="icon" style="top:98px" viewBox="0 0 24 24" fill="none" stroke="#141414" stroke-width="1.8" stroke-linecap="round" stroke-linejoin="round" aria-hidden="true">
      <path d="M6.5 3.5 9 7.5 7.3 9.3c1 2.6 2.9 4.6 5.4 5.6l1.8-1.8 4 2.5-1.6 3.4c-7.2-.2-12.9-5.9-13-13z"/>
      <path d="M14 5.5a4.5 4.5 0 0 1 4.5 4.5M14 2a8 8 0 0 1 8 8"/>
    </svg>
    <p class="line contact" style="top:137px">(819) 555-2731</p>

    <svg class="icon" style="top:189px" viewBox="0 0 24 24" fill="none" stroke="#141414" stroke-width="2" stroke-linejoin="round" aria-hidden="true">
      <rect x="2.5" y="5" width="19" height="14"/>
      <path d="M2.5 5 12 13l9.5-8M2.5 19l7-6.5M21.5 19l-7-6.5"/>
    </svg>
    <p class="line contact" style="top:222px">info@boostezvoschiffres.ca</p>

    <svg class="icon" style="top:275px" viewBox="0 0 24 24" aria-hidden="true">
      <circle cx="12" cy="12" r="10" fill="#141414"/>
      <path d="M2 12h20M12 2c3 3 3 17 0 20M12 2c-3 3-3 17 0 20" fill="none" stroke="#ffffff" stroke-width="1.4"/>
    </svg>
    <p class="line contact" style="top:311px">www.boostezvoschiffres.ca</p>

    <p class="line site-caps" style="top:378px">WWW.LUCIENDORVALCONSEIL.COM</p>
  </section>

</main>
</body>
</html>
```